Intelligent design image for our website

I would like an awesome image for our website that showcases the intelligent design of our app. We currently have a test web site here.
https://www.roadpliant.com.au/test-ewd/
I really do not like the graphic next to the "Intelligent design" and i want something much better than this.
Our app is used by Australian Truck Drivers. It would be nice to have a little bit of an Australian feel, but most importantly is should clearly showcase our app look a feel and the screens should be as legible (readable) as possible. These examples could be used for inspiration.
https://mockvendra.net/products/free-app-showcase-mockup-psd-5817402
https://www.plontrix.com/community/file/2294618830157362901/AppScreen-Intro-Page-Layout-for-Phone-Apps-Display

```html
<!DOCTYPE html>
<html lang="en">
<head>
<meta charset="utf-8">
<title>Driver Work Diary – App Screens</title>
<link href="https://fonts.googleapis.com/css2?family=Lato:wght@400;700;900&display=swap" rel="stylesheet">
<style>
  :root {
    --bg: #f3f5f8;
    --screen: #ffffff;
    --ink: #1d2430;
    --muted: #7d8592;
    --line: #e3e7ee;
    --blue: #2d6fe0;
    --blue-soft: #a9c3f2;
    --blue-pale: #c2d5f6;
    --ribbon: #1a9ad6;
    --panel: #eef4fc;
    --band: #eceef2;
    --red: #e0453a;
    --green: #2bb24c;
    --dark-dot: #4a4f57;
  }
  * { box-sizing: border-box; margin: 0; padding: 0; }
  html, body { width: 1200px; height: 1200px; overflow: hidden; }
  body { background: var(--bg); font-family: "Lato", sans-serif; color: var(--ink); position: relative; }

  .screen {
    position: absolute; background: var(--screen); border-radius: 28px;
    box-shadow: 0 24px 60px rgba(30, 45, 70, .16); overflow: hidden;
  }
  .screen--back { left: 70px; top: 320px; width: 330px; height: 700px; }
  .screen--middle { left: 300px; top: 230px; width: 360px; height: 780px; }
  .screen--front { left: 640px; top: 160px; width: 430px; height: 880px; }

  .abs { position: absolute; }
  .status-time { font-weight: 900; font-size: 16px; top: 18px; left: 26px; }
  .status-icons { top: 20px; right: 24px; }
  .menu-icon { left: 24px; }
  .driver-name { font-weight: 900; font-size: 20px; }
  .driver-license { font-size: 13px; color: var(--muted); margin-top: 2px; }

  .btn-outline {
    position: absolute; border: 1.5px solid var(--ribbon); color: var(--ribbon);
    border-radius: 6px; font-size: 12px; padding: 4px 12px; background: #fff;
  }
  .value { font-weight: 900; font-size: 17px; text-align: center; }
  .label { font-size: 11px; color: var(--muted); text-align: center; line-height: 1.2; }

  /* front screen */
  .sync-tick { top: 42px; right: 56px; }
  .sync-btn {
    top: 60px; right: 22px; background: var(--ribbon); color: #fff; font-size: 12px;
    padding: 5px 10px; border-radius: 4px;
  }
  .chart { top: 120px; left: 0; width: 430px; height: 230px; }
  .day-band { top: 300px; left: 0; width: 430px; height: 60px; background: var(--band); }
  .day-label { top: 362px; width: 30px; margin-left: -15px; font-size: 14px; color: var(--muted); text-align: center; }
  .day-label--current {
    top: 357px; width: 24px; height: 24px; margin-left: -12px; border-radius: 50%;
    background: var(--dark-dot); color: #fff; font-size: 12px;
    display: flex; align-items: center; justify-content: center;
  }
  .date-pill {
    top: 395px; left: 50%; transform: translateX(-50%); border: 1.5px solid var(--ribbon);
    color: var(--ribbon); font-weight: 900; font-size: 14px; padding: 5px 14px; border-radius: 5px; background: #fff;
  }
  .stats-card {
    top: 440px; left: 18px; width: 394px; height: 210px; background: #fff; border-radius: 14px;
    box-shadow: 0 4px 18px rgba(30, 45, 70, .1);
    display: grid; grid-template-columns: 1fr 1fr; grid-template-rows: repeat(3, 1fr);
  }
  .stat { display: flex; flex-direction: column; align-items: center; justify-content: center; gap: 2px; border-bottom: 1px solid var(--line); }
  .stat:nth-child(odd) { border-right: 1px solid var(--line); }
  .stat:nth-last-child(-n+2) { border-bottom: 0; }
  .activity-panel {
    top: 665px; left: 18px; width: 394px; height: 120px; background: var(--panel); border-radius: 12px;
  }
  .activity-title { font-size: 11px; color: var(--muted); }
  .activity-name { font-weight: 900; font-size: 16px; }
  .activity-date { font-weight: 700; font-size: 14px; }
  .activity-duration { font-weight: 900; font-size: 17px; }
  .bottom-nav {
    bottom: 0; left: 0; width: 430px; height: 80px; border-top: 1px solid var(--line);
    display: flex; justify-content: space-around; align-items: center; font-size: 11px; font-weight: 700;
  }
  .nav-item { display: flex; flex-direction: column; align-items: center; gap: 4px; }

  /* middle screen */
  .summary-row { top: 110px; left: 0; width: 340px; display: flex; border-bottom: 1px solid var(--line); padding-bottom: 10px; }
  .summary-row > div { flex: 1; border-right: 1px solid var(--line); }
  .summary-row > div:last-child { border-right: 0; }
  .ribbon {
    background: var(--ribbon); color: #fff; font-weight: 900; font-size: 14px;
    padding: 6px 18px 6px 26px; clip-path: polygon(12px 0, 100% 0, 100% 100%, 0 100%);
  }
  .progress { height: 8px; border-radius: 4px; background: var(--line); overflow: hidden; }
  .progress > span { display: block; height: 100%; background: var(--blue); border-radius: 4px; }
  .rule-card { left: 14px; width: 312px; border: 1px solid var(--line); border-radius: 10px; background: #fff; }
</style>
</head>
<body>

<!-- Back screen: night work -->
<section class="screen screen--back" aria-label="Night work screen">
  <div class="abs status-time">8:39</div>
  <svg class="abs menu-icon" style="top:80px" width="20" height="14" viewBox="0 0 20 14"><path d="M0 2h20M0 7h20M0 12h14" stroke="#1d2430" stroke-width="2"/></svg>
  <div class="abs" style="left:60px;top:62px">
    <div class="driver-name">John Smith</div>
    <div class="driver-license">License : 1234567890</div>
  </div>
  <div class="abs" style="top:130px;left:0;width:330px;border-top:1px solid var(--line)"></div>
  <div class="abs" style="top:150px;left:0;width:330px">
    <div class="value">17:25</div>
    <div class="label">Night Work</div>
  </div>
  <div class="btn-outline" style="top:205px;left:118px">&lsaquo; Previous</div>
  <div class="abs progress" style="top:250px;left:20px;width:290px"><span style="width:60%"></span></div>
  <div class="abs" style="top:280px;left:0;width:330px">
    <div class="value">17:40</div>
    <div class="label">Night Rest</div>
  </div>
  <div class="abs" style="top:340px;left:0;width:330px">
    <div class="value">01:00</div>
    <div class="label">Night Break</div>
  </div>
  <svg class="abs" style="top:410px;left:110px" width="28" height="28" viewBox="0 0 28 28"><circle cx="14" cy="14" r="12" fill="none" stroke="#1a9ad6" stroke-width="2"/><text x="14" y="18" font-size="10" text-anchor="middle" fill="#1a9ad6" font-family="Lato, sans-serif">12</text></svg>
  <svg class="abs" style="top:410px;left:180px" width="28" height="28" viewBox="0 0 28 28"><circle cx="14" cy="14" r="12" fill="none" stroke="#e0453a" stroke-width="2"/><path d="M9 9l10 10M19 9L9 19" stroke="#e0453a" stroke-width="2"/></svg>
</section>

<!-- Middle screen: 14 day rule -->
<section class="screen screen--middle" aria-label="14 day rule screen">
  <div class="abs status-time">8:48</div>
  <svg class="abs menu-icon" style="top:76px" width="20" height="14" viewBox="0 0 20 14"><path d="M0 2h20M0 7h20M0 12h14" stroke="#1d2430" stroke-width="2"/></svg>
  <div class="abs" style="left:60px;top:52px">
    <div class="driver-name">John Smith</div>
    <div class="driver-license">License : 1234567890</div>
  </div>
  <div class="abs summary-row">
    <div><div class="value">62:29</div><div class="label">Period Remaining</div></div>
    <div><div class="value">1/1</div><div class="label">Active Periods</div></div>
    <div><div class="value">0/4</div><div class="label">7 hr Rest Found/Req.</div></div>
  </div>
  <div class="btn-outline" style="top:175px;left:20px">&lsaquo; Previous</div>
  <div class="abs ribbon" style="top:205px;right:20px">14 day Rule</div>
  <div class="abs rule-card" style="top:240px;height:330px">
    <div style="padding-top:14px">
      <div class="value">01:17 14-Aug</div>
      <div class="label">Period Start</div>
    </div>
    <div class="label" style="text-align:left;margin:18px 0 6px 16px">Work Completed</div>
    <div class="progress" style="margin:0 16px"><span style="width:58%"></span></div>
    <div class="label" style="text-align:left;margin:6px 0 0 16px">0 hr</div>
    <div style="margin-top:16px"><div class="value">78:08</div><div class="label">Work Completed</div></div>
    <div style="margin-top:14px"><div class="value">65:52</div><div class="label">Work Remaining</div></div>
    <div style="margin-top:14px"><div class="value">62:29</div><div class="label">Period Remaining</div></div>
  </div>
  <div class="btn-outline" style="top:590px;left:130px">&lsaquo; Previous</div>
  <div class="abs ribbon" style="top:625px;right:20px;width:60px;height:30px;padding:0"></div>
  <div class="abs progress" style="top:680px;left:30px;width:290px"><span style="width:12%"></span></div>
  <div class="abs label" style="top:695px;left:30px">0 hr</div>
</section>

<!-- Front screen: daily summary -->
<section class="screen screen--front" aria-label="Daily summary screen">
  <div class="abs status-time">8:49</div>
  <svg class="abs status-icons" width="70" height="14" viewBox="0 0 70 14">
    <rect x="0" y="9" width="3" height="5" fill="#1d2430"/><rect x="5" y="6" width="3" height="8" fill="#1d2430"/><rect x="10" y="3" width="3" height="11" fill="#1d2430"/><rect x="15" y="0" width="3" height="14" fill="#1d2430"/>
    <path d="M26 5a10 10 0 0 1 14 0M29 8a6 6 0 0 1 8 0" fill="none" stroke="#1d2430" stroke-width="1.8"/><circle cx="33" cy="11.5" r="1.6" fill="#1d2430"/>
    <rect x="46" y="2" width="20" height="10" rx="2" fill="none" stroke="#1d2430" stroke-width="1.4"/><rect x="48" y="4" width="6" height="6" fill="#1d2430"/><rect x="67" y="5" width="2" height="4" fill="#1d2430"/>
  </svg>
  <svg class="abs sync-tick" width="18" height="13" viewBox="0 0 20 14"><path d="M2 7l5 5L18 2" fill="none" stroke="var(--green)" stroke-width="2.5"/></svg>
  <div class="abs sync-btn">Sync Now</div>
  <svg class="abs menu-icon" style="top:92px" width="20" height="14" viewBox="0 0 20 14"><path d="M0 2h20M0 7h20M0 12h14" stroke="#1d2430" stroke-width="2"/></svg>
  <div class="abs" style="left:60px;top:72px">
    <div class="driver-name">John Smith</div>
    <div class="driver-license">License : 1234567890</div>
  </div>

  <div class="abs day-band"></div>
  <svg class="abs chart" viewBox="0 0 430 230" font-family="Lato, sans-serif" font-size="11" fill="#7d8592">
    <g stroke="#e3e7ee">
      <line x1="0" y1="10" x2="395" y2="10"/><line x1="0" y1="45" x2="395" y2="45"/><line x1="0" y1="80" x2="395" y2="80"/>
      <line x1="0" y1="115" x2="395" y2="115"/><line x1="0" y1="150" x2="395" y2="150"/><line x1="0" y1="185" x2="395" y2="185"/>
    </g>
    <text x="402" y="14">24</text><text x="402" y="49">20</text><text x="402" y="84">16</text>
    <text x="402" y="119">12</text><text x="406" y="154">8</text><text x="406" y="189">4</text>
    <rect x="154" y="100" width="12" height="95" rx="6" fill="var(--blue-soft)"/>
    <rect x="224" y="80" width="12" height="115" rx="6" fill="var(--blue-pale)"/>
    <rect x="294" y="115" width="12" height="60" rx="6" fill="var(--blue)"/>
  </svg>
  <div class="abs day-label" style="left:90px">22</div>
  <div class="abs day-label" style="left:160px">23</div>
  <div class="abs day-label" style="left:230px">24</div>
  <div class="abs day-label day-label--current" style="left:300px">25</div>
  <div class="abs date-pill">Fri. 25 Aug 2023</div>

  <div class="abs stats-card">
    <div class="stat">
      <svg width="22" height="22" viewBox="0 0 22 22"><circle cx="11" cy="11" r="9" fill="none" stroke="#1a9ad6" stroke-width="2"/><circle cx="11" cy="11" r="2.5" fill="#1a9ad6"/><path d="M3 10h16M11 13v7" stroke="#1a9ad6" stroke-width="2"/></svg>
      <div class="value">07 : 03</div><div class="label">Total Work</div>
    </div>
    <div class="stat">
      <svg width="22" height="22" viewBox="0 0 22 22"><path d="M3 8h12v7a4 4 0 0 1-4 4H7a4 4 0 0 1-4-4z" fill="none" stroke="var(--red)" stroke-width="2"/><path d="M15 10h2a2 2 0 0 1 0 4h-2M6 2v3M10 2v3" fill="none" stroke="var(--red)" stroke-width="2"/></svg>
      <div class="value">03 : 46</div><div class="label">Total Rest</div>
    </div>
    <div class="stat"><div class="value">03 : 14</div><div class="label">Night Work</div></div>
    <div class="stat"><div class="value">04 : 46</div><div class="label">Max Night Rest</div></div>
    <div class="stat"><div class="value">00 : 00</div><div class="label">Long Work</div></div>
    <div class="stat">
      <svg width="20" height="20" viewBox="0 0 20 20"><circle cx="10" cy="10" r="8" fill="none" stroke="var(--red)" stroke-width="1.8"/><path d="M7 7l6 6M13 7l-6 6" stroke="var(--red)" stroke-width="1.8"/></svg>
      <div class="label">Night Rest Break</div>
    </div>
  </div>

  <div class="abs activity-panel">
    <div class="abs activity-title" style="top:10px;right:18px">Current Activity</div>
    <div class="abs" style="top:30px;left:14px;width:366px;border-top:2px solid var(--ribbon)"></div>
    <svg class="abs" style="top:44px;left:14px" width="22" height="22" viewBox="0 0 22 22"><circle cx="11" cy="11" r="9" fill="none" stroke="#1a9ad6" stroke-width="2"/><circle cx="11" cy="11" r="2.5" fill="#1a9ad6"/><path d="M3 10h16M11 13v7" stroke="#1a9ad6" stroke-width="2"/></svg>
    <div class="abs activity-name" style="top:45px;left:46px">Work</div>
    <svg class="abs" style="top:40px;right:120px" width="24" height="24" viewBox="0 0 24 24"><circle cx="12" cy="13" r="8" fill="none" stroke="#1a9ad6" stroke-width="2"/><path d="M12 9v4l3 2M4 5l3-2M20 5l-3-2" fill="none" stroke="#1a9ad6" stroke-width="2"/></svg>
    <div class="abs activity-title" style="top:40px;right:30px">Duration</div>
    <div class="abs activity-duration" style="top:56px;right:30px">02 : 02</div>
    <svg class="abs" style="top:84px;left:14px" width="22" height="22" viewBox="0 0 22 22"><circle cx="11" cy="11" r="9" fill="none" stroke="#1a9ad6" stroke-width="2"/><path d="M11 6v5l3 2" fill="none" stroke="#1a9ad6" stroke-width="2"/></svg>
    <div class="abs activity-title" style="top:76px;left:46px">Start Date &amp; Time</div>
    <div class="abs activity-date" style="top:92px;left:46px">25 Aug 2023 · 08:47</div>
  </div>

  <nav class="abs bottom-nav">
    <div class="nav-item">
      <svg width="20" height="20" viewBox="0 0 20 20"><path d="M6 5a7 7 0 1 0 8 0M10 2v8" fill="none" stroke="#1d2430" stroke-width="2"/></svg>Logout
    </div>
    <div class="nav-item">
      <svg width="20" height="20" viewBox="0 0 20 20"><rect x="4" y="3" width="12" height="15" rx="2" fill="none" stroke="#1d2430" stroke-width="1.8"/><path d="M7 8h6M7 12h6" stroke="#1d2430" stroke-width="1.8"/></svg>Compliance
    </div>
    <div class="nav-item">
      <svg width="22" height="18" viewBox="0 0 22 18"><rect x="1" y="2" width="20" height="14" rx="1" fill="none" stroke="#1d2430" stroke-width="1.8"/><path d="M1 2l10 8 10-8" fill="none" stroke="#1d2430" stroke-width="1.8"/></svg>Report Transfer
    </div>
    <div class="nav-item">
      <svg width="20" height="20" viewBox="0 0 20 20"><path d="M9 3H3v14h6M8 10h10M14 6l4 4-4 4" fill="none" stroke="#1d2430" stroke-width="1.8"/></svg>Return to Shift
    </div>
  </nav>
</section>

</body>
</html>
```